CalmHarbor Homepage and Landing Pages

Please see detailed brief.

CalmHarbor is Australia’s newest online therapy and mental health service. We allow patients from across australia to connect with Mental health practitioners from across Australia. Our mission is to remove the friction in gaining support for mental health related issues.

Number of Pages Required

1 page

Font styles to use
Sans Serif

Colors
33a6d7
0293ce
3277b5
0255a3
acd136
9bcb3c

Requirements
Must have
• Please see detailed brief.
Nice to have
• Please see detailed brief
Should not have

```html
<!DOCTYPE html>
<html lang="en">
<head>
<meta charset="utf-8">
<title>CalmHarbor Homepage</title>
<link href="https://fonts.googleapis.com/css2?family=Montserrat:wght@400;500;600;700&display=swap" rel="stylesheet">
<style>
:root{
  --sky:#33a6d7;
  --blue:#0293ce;
  --mid:#3277b5;
  --navy:#0255a3;
  --lime:#acd136;
  --ink:#2c3440;
  --muted:#7a818b;
  --soft:#f1f4f8;
  --line:#dfe4ea;
  --dark:#23272e;
  --white:#ffffff;
}
*{box-sizing:border-box;margin:0;padding:0}
html,body{width:1200px;height:3000px;overflow:hidden}
body{background:var(--blue);font-family:"Montserrat",sans-serif;color:var(--ink);position:relative}
.label{position:absolute;top:40px;color:var(--white);font-weight:600;font-size:44px;letter-spacing:4px}
.label.desk-label{left:335px}
.label.mob-label{left:880px}

.page{position:absolute;top:140px;background:var(--white);overflow:hidden}
.desktop{left:60px;width:660px}
.mobile{left:830px;width:300px}
section{position:relative;overflow:hidden}

/* shared */
.logo{display:flex;align-items:center;gap:6px;font-weight:500;color:var(--navy)}
.logo .dot{width:12px;height:12px;border-radius:50%;background:var(--blue)}
.sec-title{text-align:center;font-weight:600;color:var(--ink);font-size:14px}
.sec-title span{color:var(--blue)}
.divider{display:flex;align-items:center;justify-content:center;gap:5px;margin:6px auto 0}
.divider i{display:block;width:44px;height:1px;background:var(--line)}
.divider b{display:block;width:7px;height:7px;border:2px solid var(--sky);border-radius:50%}
.btn{display:inline-block;background:var(--navy);color:var(--white);font-size:7.5px;font-weight:600;padding:5px 12px;border-radius:2px}
.text{font-size:7.5px;line-height:1.55;color:var(--muted)}
.grey{background:var(--soft)}
.photo{display:block}
.icon{width:24px;height:24px;margin:0 auto}
.social{display:flex;gap:4px}
.social i{display:block;width:12px;height:12px;border-radius:50%;background:var(--navy)}
.slider-dots{display:flex;gap:6px;justify-content:center}
.slider-dots i{display:block;width:24px;height:5px;border:1px solid var(--sky);border-radius:3px}
.arrows{display:flex;gap:6px;justify-content:center}
.arrows i{display:block;width:16px;height:16px;border:1px solid var(--navy);border-radius:2px;position:relative}
.arrows i::after{content:"";position:absolute;left:4px;top:7px;width:7px;height:1px;background:var(--navy)}
.field{border:1px solid #4a4f57;color:#c9ced6;font-size:7px;padding:6px 7px;background:rgba(255,255,255,.03)}
.f-head{color:var(--white);font-size:12px;font-weight:500}
.f-links{list-style:none;font-size:7px;color:#dff1fb;display:grid;grid-template-columns:1fr 1fr;gap:6px 10px}
.f-links li::before{content:"○ ";font-size:5px}
.contact-row{display:flex;gap:7px;align-items:flex-start;font-size:7px;color:#e4f4fc;margin-top:9px}

/* desktop header */
.d-header{height:53px;position:relative;z-index:3}
.d-header .logo{position:absolute;left:26px;top:14px;font-size:18px}
.d-topbar{position:absolute;right:0;top:0;height:17px;display:flex}
.d-topbar .auth{background:var(--sky);color:var(--white);font-size:6.5px;padding:4px 10px}
.d-topbar .book{background:var(--navy);color:var(--white);font-size:6.5px;font-weight:600;padding:4px 12px}
.d-nav{position:absolute;right:12px;top:27px;display:flex;gap:13px;font-size:6.5px;color:var(--muted)}
.d-nav .on{color:var(--sky)}
.d-hero{height:315px}
.d-hero .hero-photo{position:absolute;right:0;top:-53px;width:350px;height:368px}
.d-hero .copy{position:absolute;left:26px;top:60px;width:260px}
.d-hero h1{font-size:35px;font-weight:500;color:var(--mid)}
.d-hero .sub{font-size:7.5px;color:var(--blue);margin:7px 0 10px;line-height:1.5}
.d-hero .btn{margin-top:12px}

.d-services{height:315px;padding-top:40px}
.svc-grid{display:grid;grid-template-columns:repeat(3,1fr);gap:24px 30px;padding:22px 40px 0}
.svc{text-align:center}
.svc h3{font-size:7.5px;font-weight:600;margin:8px 0 5px}

.d-about{height:322px;padding-top:40px}
.d-about .circles{position:absolute;left:24px;top:100px;width:240px;height:200px}
.d-about .copy{position:absolute;left:290px;top:102px;width:350px}
.about-h{font-size:10px;font-weight:600;color:var(--blue);line-height:1.35;margin-bottom:6px}
.d-about .text{margin-bottom:8px}

.d-team{height:308px;padding-top:30px}
.team-row{display:flex;gap:16px;padding:28px 34px 0}
.member{width:136px;position:relative}
.member .photo{height:120px}
.member .cap{position:relative;width:114px;margin:-20px auto 0;background:var(--white);border:1px solid var(--line);text-align:center;padding:5px 0 6px}
.member .social{justify-content:center;margin-top:-11px;margin-bottom:4px}
.member h4{font-size:7.5px;color:var(--navy);font-weight:600}
.member p{font-size:6px;color:var(--muted);font-style:italic}

.d-testi{height:294px;padding-top:36px;text-align:center}
.avatar{width:34px;height:34px;margin:14px auto 14px}
.d-testi .text{width:580px;margin:0 auto}
.who{font-size:8px;color:var(--sky);margin-top:12px}
.who-sub{font-size:5.5px;color:var(--muted);margin:2px 0 10px}

.d-blog{height:333px;padding-top:36px}
.blog-row{display:flex;gap:16px;padding:20px 30px 0}
.post{width:188px;border:1px solid var(--line);background:var(--white)}
.post .photo{height:100px}
.post .body{padding:8px 10px 10px}
.post h4{font-size:8px;font-weight:600}
.post .by{font-size:5.5px;color:var(--muted);margin:2px 0}
.post .meta{font-size:5.5px;color:var(--ink);margin-bottom:6px}
.post .more{font-size:7px;color:var(--blue);font-weight:600;margin-top:5px}

.d-book{height:311px;background:linear-gradient(160deg,#2f343c,#1f2329);padding-top:24px;text-align:center}
.book-h{font-size:12px;color:var(--white);font-weight:600}
.book-h span{color:var(--blue)}
.d-book .lead{font-size:7px;color:#d4d8de;margin:14px 0 16px}
.d-form{display:grid;grid-template-columns:1fr 1fr;gap:8px 14px;width:345px;margin:0 auto;text-align:left}
.d-form .msg{grid-column:1/3;height:56px}
.d-book .btn{margin-top:14px;background:var(--blue)}

.d-footer{height:126px;background:var(--blue);padding:28px 26px 0;display:flex;gap:40px;color:var(--white)}
.d-footer .logo{color:var(--white);font-size:16px}
.d-footer .logo .dot{background:var(--white)}
.copy-small{font-size:5.5px;color:#e6f4fb;margin:8px 0 8px;line-height:1.5}
.d-footer .social i{background:rgba(255,255,255,.85)}

/* mobile */
.m-header{height:28px;display:flex;align-items:center;padding:0 8px;gap:10px}
.m-header .auth{font-size:5.5px;color:var(--navy)}
.m-header .logo{font-size:14px}
.m-header .burger{margin-left:auto;width:14px;height:9px;border-top:2px solid var(--blue);border-bottom:2px solid var(--blue);position:relative}
.m-header .burger::after{content:"";position:absolute;left:0;right:0;top:1.5px;height:2px;background:var(--blue)}
.m-hero{height:168px}
.m-hero .photo{position:absolute;inset:0}
.m-hero .panel{position:absolute;left:5px;top:38px;width:180px;padding:8px;background:rgba(30,34,40,.82)}
.m-hero h1{font-size:17px;color:var(--white);font-weight:500}
.m-hero .sub{font-size:6.5px;color:var(--sky);margin:3px 0 7px;line-height:1.35}
.m-hero .btn{font-size:6px;padding:4px 8px}
.m-services{height:218px;padding-top:22px;text-align:center}
.m-services .svc{margin:18px 30px 0}
.m-services .btn{margin-top:10px}
.m-about{height:500px;padding-top:24px}
.m-about .circles{width:230px;height:172px;margin:18px auto 0}
.m-about .copy{padding:14px 12px 0}
.m-about .text{margin-bottom:8px}
.m-about .center{text-align:center}
.m-team{height:364px;padding-top:22px}
.m-team .member{width:186px;margin:16px auto 0}
.m-team .member .photo{height:190px}
.m-team .member .cap{width:170px;margin-top:-30px;padding-bottom:9px}
.m-team .member .social i{width:16px;height:16px}
.m-team .member .social{margin-top:-14px}
.m-team .member h4{font-size:10px}
.m-team .member p{font-size:7.5px}
.m-team .arrows{margin-top:12px}
.m-testi{height:266px;padding-top:20px;text-align:center}
.m-testi .text{padding:0 10px}
.m-blog{height:347px;padding-top:20px}
.m-blog .post{width:218px;margin:16px auto 0}
.m-blog .post .photo{height:118px}
.m-blog .arrows{margin-top:10px}
.m-book{height:395px;background:linear-gradient(160deg,#2f343c,#1f2329);padding-top:24px;text-align:center}
.m-book .lead{font-size:7px;color:#d4d8de;margin:14px 16px 12px;line-height:1.4}
.m-form{display:grid;gap:8px;width:222px;margin:0 auto;text-align:left}
.m-form .msg{height:54px}
.m-book .btn{margin-top:12px;background:var(--blue)}
.m-footer{height:365px;background:var(--blue);padding:22px 18px 0;color:var(--white)}
.m-footer .logo{justify-content:center;color:var(--white);font-size:18px}
.m-footer .logo .dot{background:var(--white)}
.m-footer .f-head{font-size:14px;margin:16px 0 12px}
.m-footer .social{margin-top:12px}
.m-footer .social i{background:rgba(255,255,255,.85)}
.m-footer .copy-small{margin-top:14px}
</style>
</head>
<body>

<div class="label desk-label">DESKTOP</div>
<div class="label mob-label">MOBILE</div>

<!-- ================= DESKTOP ================= -->
<main class="page desktop">
  <header class="d-header">
    <div class="logo"><span class="dot"></span>CalmHarbor</div>
    <div class="d-topbar"><span class="auth">Login &nbsp; Register</span><span class="book">Book An Appointment</span></div>
    <nav class="d-nav"><span class="on">Home</span><span>About Us</span><span>Services</span><span>Practitioner Information</span><span>Our Team</span><span>Contact Us</span></nav>
  </header>

  <section class="d-hero">
    <svg class="hero-photo" viewBox="0 0 350 368" role="img" aria-label="Physiotherapist treating a patient's leg on a treatment table">
      <defs><linearGradient id="heroG" x1="0" y1="0" x2="1" y2="1"><stop offset="0" stop-color="#d9dde2"/><stop offset=".55" stop-color="#9ea7b1"/><stop offset="1" stop-color="#6d6459"/></linearGradient></defs>
      <path d="M60 50 C20 90 70 140 30 200 C0 260 20 330 90 360 L350 320 L350 50 Z" fill="url(#heroG)"/>
      <path d="M90 360 C180 350 260 330 350 300" stroke="#0293ce" stroke-width="3" fill="none"/>
      <path d="M70 40 C40 70 55 100 40 130" stroke="#e6eaef" stroke-width="14" fill="none"/>
    </svg>
    <div class="copy">
      <h1>CalmHarbor</h1>
      <p class="sub">CalmHarbor is Australia's newest online therapy and mental health service.</p>
      <p class="text">But I must explain to you how all this mistaken idea of denouncing pleasure and praising pain was born and I will give you a complete account of the system.</p>
      <span class="btn">Contact Us</span>
    </div>
  </section>

  <section class="d-services">
    <h2 class="sec-title">Our <span>Services</span></h2>
    <div class="divider"><i></i><b></b><i></i></div>
    <div class="svc-grid">
      <div class="svc"><svg class="icon" viewBox="0 0 24 24"><circle cx="12" cy="11" r="8" fill="none" stroke="#0293ce" stroke-width="1.5"/><path d="M8 21h8" stroke="#0293ce" stroke-width="1.5"/></svg><h3>MENTAL HEALTH</h3><p class="text">But I must explain to you how all this mistaken idea of denouncing pleasure and praising pain was born complete.</p></div>
      <div class="svc"><svg class="icon" viewBox="0 0 24 24"><rect x="3" y="13" width="18" height="5" fill="none" stroke="#0293ce" stroke-width="1.5"/><circle cx="12" cy="7" r="3" fill="none" stroke="#0293ce" stroke-width="1.5"/></svg><h3>PHYSICAL THERAPY</h3><p class="text">But I must explain to you how all this mistaken idea of denouncing pleasure and praising pain was born complete.</p></div>
      <div class="svc"><svg class="icon" viewBox="0 0 24 24"><circle cx="7" cy="7" r="3" fill="none" stroke="#0293ce" stroke-width="1.5"/><circle cx="17" cy="7" r="3" fill="none" stroke="#0293ce" stroke-width="1.5"/><path d="M4 21v-8h6v8M14 21v-8h6v8" fill="none" stroke="#0293ce" stroke-width="1.5"/></svg><h3>FAMILY THERAPY</h3><p class="text">But I must explain to you how all this mistaken idea of denouncing pleasure and praising pain was born complete.</p></div>
      <div class="svc"><svg class="icon" viewBox="0 0 24 24"><circle cx="12" cy="5" r="2.5" fill="none" stroke="#0293ce" stroke-width="1.5"/><path d="M4 21l8-13 8 13M7 16h10" fill="none" stroke="#0293ce" stroke-width="1.5"/></svg><h3>PILATES THERAPY</h3><p class="text">But I must explain to you how all this mistaken idea of denouncing pleasure and praising pain was born complete.</p></div>
      <div class="svc"><svg class="icon" viewBox="0 0 24 24"><path d="M12 3v18M5 10l7 4 7-4" fill="none" stroke="#0293ce" stroke-width="1.5"/><circle cx="12" cy="6" r="2" fill="none" stroke="#0293ce" stroke-width="1.5"/></svg><h3>ACUPUNCTURE</h3><p class="text">But I must explain to you how all this mistaken idea of denouncing pleasure and praising pain was born complete.</p></div>
      <div class="svc"><svg class="icon" viewBox="0 0 24 24"><path d="M4 20C4 10 12 4 20 4C20 12 14 20 4 20ZM4 20L14 10" fill="none" stroke="#0293ce" stroke-width="1.5"/></svg><h3>HERBAL THERAPY</h3><p class="text">But I must explain to you how all this mistaken idea of denouncing pleasure and praising pain was born complete.</p></div>
    </div>
  </section>

  <section class="d-about grey">
    <h2 class="sec-title">Abutus <span>CalmHarbor</span></h2>
    <div class="divider"><i></i><b></b><i></i></div>
    <svg class="circles" viewBox="0 0 240 200" role="img" aria-label="Patients receiving physiotherapy and exercise care">
      <circle cx="85" cy="85" r="80" fill="#d8c9c2" stroke="#c7ccd3" stroke-dasharray="3 3"/>
      <circle cx="170" cy="135" r="62" fill="#8fa6c4" stroke="#ffffff" stroke-width="3"/>
    </svg>
    <div class="copy">
      <h3 class="about-h">PHYSIOTHERAPY SERVICES FROM PROFESSIONALS THERAPISTS</h3>
      <p class="text">Sed ut perspiciatis unde omnis iste natus error sit voluptatem accusantium doloremque laudantium, totam rem aperiam, eaque ipsa quae ab illo inventore veritatis et quasi architecto beatae vitae dicta sunt explicabo.</p>
      <p class="text">Lorem ipsum dolor sit amet, consectetur adipiscing elit, sed do eiusmod tempor incididunt ut labore et dolore magna aliqua. Ut enim ad minim veniam, quis nostrud exercitation ullamco laboris nisi ut aliquip ex ea commodo consequat. Duis aute irure dolor in reprehenderit in voluptate velit esse cillum dolore eu fugiat nulla pariatur.</p>
      <p class="text">But I must explain to you how all this mistaken idea of denouncing pleasure and praising pain was born and I will give you a complete account of the system, and expound the actual teachings of the great explorer of the truth, the master-builder of human happiness.</p>
      <span class="btn">More About Me</span>
    </div>
  </section>

  <section class="d-team">
    <h2 class="sec-title">Our <span>Team</span></h2>
    <div class="divider"><i></i><b></b><i></i></div>
    <div class="team-row">
      <div class="member"><div class="photo" role="img" aria-label="Portrait of a female doctor holding a folder" style="background:linear-gradient(160deg,#eef1f4,#c9ced6)"></div><div class="cap"><div class="social"><i></i><i></i><i></i><i></i></div><h4>Nora T. Avery</h4><p>Lorem ipsum dolor sit amet</p></div></div>
      <div class="member"><div class="photo" role="img" aria-label="Portrait of a male doctor with stethoscope" style="background:linear-gradient(160deg,#eef1f4,#b9c3cf)"></div><div class="cap"><div class="social"><i></i><i></i><i></i><i></i></div><h4>Owen R. Hale</h4><p>Lorem ipsum dolor sit amet</p></div></div>
      <div class="member"><div class="photo" role="img" aria-label="Portrait of a smiling female doctor" style="background:linear-gradient(160deg,#f4f5f7,#d3d6db)"></div><div class="cap"><div class="social"><i></i><i></i><i></i><i></i></div><h4>Maya L. Porter</h4><p>Lorem ipsum dolor sit amet</p></div></div>
      <div class="member"><div class="photo" role="img" aria-label="Portrait of a senior male doctor" style="background:linear-gradient(160deg,#e6eaef,#aeb8c4)"></div><div class="cap"><div class="social"><i></i><i></i><i></i><i></i></div><h4>Victor S. Lane</h4><p>Lorem ipsum dolor sit amet</p></div></div>
    </div>
  </section>

  <section class="d-testi grey">
    <h2 class="sec-title">Happy Client <span>are Saying</span></h2>
    <div class="divider"><i></i><b></b><i></i></div>
    <div class="avatar" role="img" aria-label="Client avatar" style="background:linear-gradient(#bfe3f4,#5aaedb)"></div>
    <p class="text">Sed ut perspiciatis unde omnis iste natus error sit voluptatem accusantium doloremque laudantium, totam rem aperiam, eaque ipsa quae ab illo inventore veritatis et quasi architecto beatae vitae dicta sunt explicabo. Nemo enim ipsam voluptatem quia voluptas sit aspernatur aut odit aut fugit, sed quia consequuntur magni dolores eos qui ratione voluptatem sequi nesciunt. Neque porro quisquam est, qui dolorem ipsum quia dolor sit amet.</p>
    <p class="who">DANIEL CRANE</p>
    <p class="who-sub">LOREM IPSUM DOLOR SIT AMET</p>
    <div class="slider-dots"><i></i><i></i><i></i></div>
  </section>

  <section class="d-blog">
    <h2 class="sec-title">Latest <span>Blog</span></h2>
    <div class="divider"><i></i><b></b><i></i></div>
    <div class="blog-row">
      <article class="post"><div class="photo" role="img" aria-label="Doctor examining a patient" style="background:linear-gradient(160deg,#dfe3e8,#8d96a2)"></div><div class="body"><h4>Health Checkup Body</h4><p class="by">Posted by Lena Marsh</p><p class="meta">Jan 15, 2020 / Leave a Comment</p><p class="text">Lorem ipsum dolor sit amet, consectetur adipiscing elit, sed do eiusmod tempor incididunt ut labore et dolore.</p><p class="more">Read More ›</p></div></article>
      <article class="post"><div class="photo" role="img" aria-label="Physical therapy session in a clinic" style="background:linear-gradient(160deg,#e7f1f8,#7fb3d8)"></div><div class="body"><h4>Physical Therapy</h4><p class="by">Posted by Lena Marsh</p><p class="meta">Jan 23, 2020 / Leave a Comment</p><p class="text">Lorem ipsum dolor sit amet, consectetur adipiscing elit, sed do eiusmod tempor incididunt ut labore et dolore.</p><p class="more">Read More ›</p></div></article>
      <article class="post"><div class="photo" role="img" aria-label="Therapist working with a patient" style="background:linear-gradient(160deg,#e4e7eb,#9a8f87)"></div><div class="body"><h4>Lorem ipsum dolor sit amet</h4><p class="by">Posted by Lena Marsh</p><p class="meta">Jan 26, 2020 / Leave a Comment</p><p class="text">Lorem ipsum dolor sit amet, consectetur adipiscing elit, sed do eiusmod tempor incididunt ut labore et dolore.</p><p class="more">Read More ›</p></div></article>
    </div>
  </section>

  <section class="d-book">
    <h2 class="book-h">BOOK AN <span>APPOINTMENT</span></h2>
    <div class="divider"><i style="background:#4a4f57"></i><b></b><i style="background:#4a4f57"></i></div>
    <p class="lead">Sed ut perspiciatis unde omnis iste natus error sit voluptatem accusantium doloremque laudantium</p>
    <div class="d-form">
      <div class="field">First Name</div><div class="field">Email Address</div>
      <div class="field">Your Subject</div><div class="field">Phone</div>
      <div class="field">Appointment Date</div><div class="field">Appointment Time</div>
      <div class="field msg">Message</div>
    </div>
    <span class="btn">SUBMIT</span>
  </section>

  <footer class="d-footer">
    <div>
      <div class="logo"><span class="dot"></span>CalmHarbor</div>
      <p class="copy-small">Copyright © 2020 CalmHarbor<br>All Right Reserved</p>
      <div class="social"><i></i><i></i><i></i><i></i><i></i></div>
    </div>
    <div>
      <h3 class="f-head">Important Links</h3>
      <ul class="f-links" style="margin-top:10px"><li>Home</li><li>About Us</li><li>Services</li><li>Practitioner Information</li><li>Our Team</li><li>Contact Us</li><li>Term &amp; Condition</li><li>Privacy Policy</li></ul>
    </div>
    <div>
      <h3 class="f-head">Contact Information</h3>
      <div class="contact-row"><svg width="10" height="10" viewBox="0 0 10 10"><path d="M5 9.5C2 6 1.5 5 1.5 3.8a3.5 3.5 0 017 0C8.5 5 8 6 5 9.5Z" fill="none" stroke="#fff"/></svg><span>48 Tidewater Lane,<br>Hobart, TAS 7000</span></div>
      <div class="contact-row"><svg width="10" height="10" viewBox="0 0 10 10"><path d="M2 1l2 2-1 1.5c.8 1.5 1.5 2.2 3 3L7.5 6l2 2-1.5 1.5C4 9 1 6 .5 2.5Z" fill="none" stroke="#fff"/></svg><span>(03) 5550 1829</span></div>
      <div class="contact-row"><svg width="10" height="10" viewBox="0 0 10 10"><rect x=".5" y="2" width="9" height="6" fill="none" stroke="#fff"/><path d="M.5 2L5 5.5 9.5 2" fill="none" stroke="#fff"/></svg><span>hello@calmharbor.example</span></div>
    </div>
  </footer>
</main>

<!-- ================= MOBILE ================= -->
<main class="page mobile">
  <header class="m-header">
    <span class="auth">Login &nbsp;Register</span>
    <div class="logo"><span class="dot"></span>CalmHarbor</div>
    <span class="burger"></span>
  </header>

  <section class="m-hero">
    <div class="photo" role="img" aria-label="Physiotherapist treating a patient's leg on a treatment table" style="background:linear-gradient(160deg,#dde1e6,#98a1ab 60%,#6f665c)"></div>
    <div class="panel">
      <h1>CalmHarbor</h1>
      <p class="sub">CalmHarbor is Australia's newest online therapy and mental health service</p>
      <span class="btn">Contact Us</span>
    </div>
  </section>

  <section class="m-services">
    <h2 class="sec-title">Our <span>Services</span></h2>
    <div class="divider"><i></i><b></b><i></i></div>
    <div class="svc"><svg class="icon" viewBox="0 0 24 24"><circle cx="12" cy="11" r="8" fill="none" stroke="#0293ce" stroke-width="1.5"/><path d="M8 21h8" stroke="#0293ce" stroke-width="1.5"/></svg><h3>MENTAL HEALTH</h3><p class="text">But I must explain to you how all this mistaken idea of denouncing pleasure and praising pain was born complete.</p></div>
    <span class="btn">Show More</span>
  </section>

  <section class="m-about grey">
    <h2 class="sec-title">Abutus <span>CalmHarbor</span></h2>
    <div class="divider"><i></i><b></b><i></i></div>
    <svg class="circles" viewBox="0 0 230 172" role="img" aria-label="Patients receiving physiotherapy and exercise care" style="display:block">
      <circle cx="82" cy="80" r="76" fill="#d8c9c2" stroke="#c7ccd3" stroke-dasharray="3 3"/>
      <circle cx="164" cy="115" r="56" fill="#8fa6c4" stroke="#ffffff" stroke-width="3"/>
    </svg>
    <div class="copy">
      <h3 class="about-h">PHYSIOTHERAPY SERVICES FROM PROFESSIONALS THERAPISTS</h3>
      <p class="text">Sed ut perspiciatis unde omnis iste natus error sit voluptatem accusantium doloremque laudantium, totam rem aperiam, eaque ipsa quae ab illo inventore veritatis et quasi architecto beatae vitae dicta sunt explicabo.</p>
      <p class="text">Lorem ipsum dolor sit amet, consectetur adipiscing elit, sed do eiusmod tempor incididunt ut labore et dolore magna aliqua. Ut enim ad minim veniam, quis nostrud exercitation ullamco laboris nisi ut aliquip ex ea commodo consequat. Duis aute irure dolor in reprehenderit in voluptate velit esse cillum dolore eu fugiat nulla pariatur.</p>
      <p class="text">But I must explain to you how all this mistaken idea of denouncing pleasure and praising pain was born and I will give you a complete account of the system, and expound the actual teachings.</p>
      <div class="center"><span class="btn">More About Me</span></div>
    </div>
  </section>

  <section class="m-team">
    <h2 class="sec-title">Our <span>Team</span></h2>
    <div class="divider"><i></i><b></b><i></i></div>
    <div class="member"><div class="photo" role="img" aria-label="Portrait of a male doctor with stethoscope" style="background:linear-gradient(160deg,#eef1f4,#b9c3cf)"></div><div class="cap"><div class="social"><i></i><i></i><i></i><i></i></div><h4>Owen R. Hale</h4><p>Lorem ipsum dolor sit amet</p></div></div>
    <div class="arrows"><i style="transform:scaleX(-1)"></i><i></i></div>
  </section>

  <section class="m-testi grey">
    <h2 class="sec-title">Happy Client <span>are Saying</span></h2>
    <div class="divider"><i></i><b></b><i></i></div>
    <div class="avatar" role="img" aria-label="Client avatar" style="background:linear-gradient(#bfe3f4,#5aaedb)"></div>
    <p class="text">Sed ut perspiciatis unde omnis iste natus error sit voluptatem accusantium doloremque laudantium, totam rem aperiam, eaque ipsa quae ab illo inventore veritatis et quasi architecto beatae vitae dicta sunt explicabo. Nemo enim ipsam voluptatem quia voluptas sit aspernatur aut odit aut fugit, sed quia consequuntur</p>
    <p class="who">DANIEL CRANE</p>
    <p class="who-sub">LOREM IPSUM DOLOR SIT AMET</p>
    <div class="slider-dots"><i></i><i></i><i></i></div>
  </section>

  <section class="m-blog">
    <h2 class="sec-title">Latest <span>Blog</span></h2>
    <div class="divider"><i></i><b></b><i></i></div>
    <article class="post"><div class="photo" role="img" aria-label="Doctor examining a patient" style="background:linear-gradient(160deg,#dfe3e8,#8d96a2)"></div><div class="body"><h4>Health Checkup Body</h4><p class="by">Posted by Lena Marsh</p><p class="meta">Jan 15, 2020 / Leave a Comment</p><p class="text">Lorem ipsum dolor sit amet, consectetur adipiscing elit, sed do eiusmod tempor incididunt ut labore et dolore.</p><p class="more">Read More ›</p></div></article>
    <div class="arrows"><i style="transform:scaleX(-1)"></i><i></i></div>
  </section>

  <section class="m-book">
    <h2 class="book-h">BOOK AN <span>APPOINTMENT</span></h2>
    <div class="divider"><i style="background:#4a4f57"></i><b></b><i style="background:#4a4f57"></i></div>
    <p class="lead">Sed ut perspiciatis unde omnis iste natus error sit voluptatem accusantium doloremque laudantium</p>
    <div class="m-form">
      <div class="field">First Name</div>
      <div class="field">Email Address</div>
      <div class="field">Your Subject</div>
      <div class="field">Phone</div>
      <div class="field">Appointment Date</div>
      <div class="field">Appointment Time</div>
      <div class="field msg">Message</div>
    </div>
    <span class="btn">SUBMIT</span>
  </section>

  <footer class="m-footer">
    <div class="logo"><span class="dot"></span>CalmHarbor</div>
    <h3 class="f-head">Important Links</h3>
    <ul class="f-links"><li>Home</li><li>About Us</li><li>Services</li><li>Practitioner Information</li><li>Our Team</li><li>Contact Us</li><li>Term &amp; Condition</li><li>Privacy Policy</li></ul>
    <h3 class="f-head">Contact Information</h3>
    <div class="contact-row"><svg width="10" height="10" viewBox="0 0 10 10"><path d="M5 9.5C2 6 1.5 5 1.5 3.8a3.5 3.5 0 017 0C8.5 5 8 6 5 9.5Z" fill="none" stroke="#fff"/></svg><span>48 Tidewater Lane,<br>Hobart, TAS 7000</span></div>
    <div class="contact-row"><svg width="10" height="10" viewBox="0 0 10 10"><path d="M2 1l2 2-1 1.5c.8 1.5 1.5 2.2 3 3L7.5 6l2 2-1.5 1.5C4 9 1 6 .5 2.5Z" fill="none" stroke="#fff"/></svg><span>(03) 5550 1829</span></div>
    <div class="contact-row"><svg width="10" height="10" viewBox="0 0 10 10"><rect x=".5" y="2" width="9" height="6" fill="none" stroke="#fff"/><path d="M.5 2L5 5.5 9.5 2" fill="none" stroke="#fff"/></svg><span>hello@calmharbor.example</span></div>
    <div class="social"><i></i><i></i><i></i><i></i><i></i></div>
    <p class="copy-small">Copyright © 2020 CalmHarbor. All Right Reserved.</p>
  </footer>
</main>

</body>
</html>
```